CD cover for rock-nproll song

I need a logo design for a CD cover for a soon-to-be released rock song by my band, LURK.
The song is called "Honey Don't Wait". The logo should include the band logo as well as some representation of the song title. The song is about the end of a romantic relationship.

Target Market(s)

on -line music consumers

Industry/Entity Type

Baby

Requirements
Must have
• LURK logo (provided)
• Name of song- "Honey Don't Wait"
Nice to have
• A design that reflects the meaning in the song... "Honey Don't Wait, it's time to go, it's all over. What you said to me, made me see we've got nothing". That is the chorus- the song is about a relationship coming apart.

```html
<!DOCTYPE html>
<html lang="en">
<head>
<meta charset="utf-8">
<title>Honey Don't Wait — LURK</title>
<link rel="stylesheet" href="https://fonts.googleapis.com/css2?family=Great+Vibes&family=Questrial&display=swap">
<style>
  :root {
    --page: #ffffff;
    --frame-line: #1a1a1a;
    --sepia-top: #5e4a22;
    --sepia-mid: #8a7a3e;
    --glow: #dcdc98;
    --sepia-low: #6a4420;
    --shadow-deep: #1c1008;
    --title: #ffffff;
    --lyric: #2b2010;
    --label: #ffffff;
  }
  * { margin: 0; padding: 0; box-sizing: border-box; }
  html, body {
    width: 1200px;
    height: 1200px;
    overflow: hidden;
    background: var(--page);
  }
  .canvas {
    position: relative;
    width: 1200px;
    height: 1200px;
    background: var(--page);
    border: 1px solid var(--frame-line);
  }
  .cover {
    position: absolute;
    left: 110px;
    top: 110px;
    width: 980px;
    height: 980px;
    overflow: hidden;
  }
  .cover-photo {
    position: absolute;
    inset: 0;
    background:
      radial-gradient(ellipse 55% 30% at 42% 52%, rgba(220,220,152,0.85) 0%, rgba(220,220,152,0) 100%),
      linear-gradient(180deg,
        var(--sepia-top) 0%,
        var(--sepia-mid) 30%,
        #b8b06a 48%,
        #9a7a3c 62%,
        var(--sepia-low) 74%,
        #3a2210 86%,
        var(--shadow-deep) 100%);
  }
  .song-title {
    position: absolute;
    top: 152px;
    left: 0;
    width: 100%;
    text-align: center;
    font-family: "Great Vibes", cursive;
    font-size: 112px;
    line-height: 1;
    color: var(--title);
    white-space: nowrap;
  }
  .chorus {
    position: absolute;
    top: 334px;
    left: 0;
    width: 100%;
    text-align: center;
    font-family: "Questrial", sans-serif;
    font-size: 18px;
    line-height: 23px;
    color: var(--lyric);
  }
  .band-mark {
    position: absolute;
    top: 858px;
    left: 0;
    width: 100%;
    text-align: center;
    font-family: "Questrial", sans-serif;
    font-size: 33px;
    letter-spacing: 0.5px;
    color: var(--label);
  }
</style>
</head>
<body>
  <main class="canvas">
    <section class="cover">
      <div class="cover-photo" role="img" aria-label="Sepia photograph of a couple seen from behind, sitting on a wooden bench facing hills and water at sunset"></div>
      <h1 class="song-title">Honey Don't Wait</h1>
      <p class="chorus">It’s time to go, it’s all over. What you said to me,<br>made me see we’ve got nothing”</p>
      <p class="band-mark">LURK LOGO</p>
    </section>
  </main>
</body>
</html>
```